3 out of 100 people will get deadly skin cancer - we need a great illustration that shows this!

We put together a prototype image that communicates lifetime skin cancer risk. (see attached). We are looking for illustrators who can take make a new/better/cooler graphic that communicates this idea. It could be as simple as a superior illustration of the graphic we have or illustrators can propose a completely different idea.What should the illustration communicate?U.S. adults have a lifetime risk of developing skin cancer of 1 in 5. But we don't want to show 1 in 5; we want to show that number in a larger group. For example, in the attached illustration we show 20 in 100 people get skin cancer (i.e., 100 beach towels/umbrellas and 20 of them are red). Research has shown that people are more likely to accurately understand numbers like this when you convey them for larger groups (i.e., 20 out of 100 rather than 1 out of 5). U.S. adults also have a lifetime risk of 2.3% of developing the deadliest form of skin cancer (melanoma). In other words, approximately 3 in 100 people will develop melanoma in their lifetime. Ideally, a single image will convey both lifetime skin cancer risk (20 in 100) and melanoma risk (3 in 100). We will award a top three as follows: 1st place = $300, 2nd place = $250, third place = $200. We will also buy any design beyond 3rd place that we like for $100. For example, we purchased 24 designs in our last contest on Artmarketly.This research is supported by funding from the Corvane Institute of Science.

Target Market(s)

The U.S. public; individuals at high risk of developing skin cancer

Industry/Entity Type

Medicine

Colors

Designer to choose colors to be used in the design.

Requirements
Must have
• an original illustration that conveys both lifetime risk of developing skin cancer (20 in 100) and melanoma (3 in 100).
Nice to have
• It can be beach towels and umbrellas, just like our prototype, or the designers can pitch an original idea. Imagery can be realistic or cartoonish (or something in between). It should be illustrations, though. Not edited photos. The image should be in color (no black and white illustrations).
Should not have
• Photos. Clip art. Free vector images.
• We are looking for original illustrations created by the designer.

```html
<!DOCTYPE html>
<html lang="en">
<head>
<meta charset="utf-8">
<title>Skin Cancer – Lifetime Risk and Prevention</title>
<link rel="stylesheet" href="https://fonts.googleapis.com/css2?family=Montserrat:wght@600;700;800&family=Open+Sans:wght@400;600&display=swap">
<style>
  :root {
    --c-page: #ffffff;
    --c-mint: #7fe3a0;
    --c-lemon: #f7f27a;
    --c-peach: #ffc978;
    --c-pink: #f79ad2;
    --c-magenta: #e0117f;
    --c-violet: #8a2be2;
    --c-navy: #14215e;
    --c-orange: #ff8a2a;
    --c-red: #e8283c;
    --c-sand: #f3dfb8;
    --c-sea: #7cc9e8;
    --c-frame: #8a5a3a;
    --c-towel: #f2a64c;
    --c-cancer: #e83a2a;
    --c-melanoma: #6e0d1d;
    --c-white: #ffffff;
    --c-ink: #1b1b3a;
  }
  * { box-sizing: border-box; margin: 0; padding: 0; }
  html, body { width: 1200px; height: 4500px; overflow: hidden; background: var(--c-page); }
  body { font-family: "Open Sans", Arial, sans-serif; color: var(--c-white); }

  .poster {
    position: absolute; left: 12px; top: 12px; width: 1176px; height: 4476px;
    border-radius: 44px; overflow: hidden;
    background: linear-gradient(180deg,
      #a8ecc0 0px, var(--c-lemon) 500px, var(--c-peach) 900px, var(--c-sand) 1100px,
      var(--c-sand) 2300px, var(--c-orange) 2380px, var(--c-red) 2900px,
      var(--c-magenta) 3350px, var(--c-violet) 3750px, #2c3fd0 4150px, var(--c-navy) 4476px);
  }
  .poster::before {
    content: ""; position: absolute; inset: 0 0 auto 0; height: 1000px;
    background: linear-gradient(90deg, rgba(127,227,160,.55) 0%, rgba(247,242,122,0) 45%, rgba(247,154,210,.8) 100%);
  }
  .abs { position: absolute; }
  .heading { font-family: "Montserrat", Arial, sans-serif; font-weight: 800; }

  .title { left: 0; width: 1176px; top: 28px; text-align: center; font-size: 50px; color: var(--c-white); text-shadow: 0 2px 6px rgba(0,0,0,.15); }
  .title-rule { left: 428px; top: 96px; width: 320px; height: 8px; background: var(--c-white); border-radius: 4px; }

  .bubble { border-radius: 70px; display: flex; align-items: center; justify-content: center; text-align: center; padding: 0 50px; }
  .bubble--cause { left: 196px; top: 150px; width: 640px; height: 220px; background: var(--c-magenta); font-family: "Montserrat", sans-serif; font-weight: 700; font-size: 32px; line-height: 1.3; }
  .bubble-pill { left: 748px; top: 196px; width: 56px; height: 22px; border-radius: 11px; background: var(--c-white); border: 6px solid var(--c-red); }
  .bubble--exposure { left: 228px; top: 392px; width: 590px; height: 210px; background: var(--c-navy); font-weight: 600; font-size: 32px; line-height: 1.3; }
  .dot { border-radius: 50%; background: var(--c-navy); }
  .dot--a { left: 224px; top: 610px; width: 34px; height: 34px; }
  .dot--b { left: 196px; top: 648px; width: 20px; height: 20px; }

  .art { border-radius: 30px; }
  .art--bolt { left: 40px; top: 220px; width: 140px; height: 260px; background: linear-gradient(160deg, #ff3b8a, #7b2be0); border-radius: 20px; }
  .art--walker { left: 850px; top: 110px; width: 310px; height: 500px; background: linear-gradient(180deg, #f7c9a6, #f2543a); }
  .art--lounger { left: 0; top: 630px; width: 400px; height: 380px; background: linear-gradient(180deg, #f4d9a0, #c9924f); border-radius: 0 30px 30px 0; }

  .ask { font-family: "Montserrat", sans-serif; font-weight: 700; color: var(--c-white); }
  .ask--likely { left: 400px; top: 668px; width: 760px; height: 106px; border-radius: 53px; background: linear-gradient(90deg, #c44bd8, #6a5bea); display: flex; align-items: center; padding-left: 40px; font-size: 36px; }
  .ask--beach { left: 560px; top: 790px; width: 600px; font-size: 30px; font-weight: 600; color: var(--c-white); text-shadow: 0 1px 4px rgba(0,0,0,.25); }
  .ask--count { left: 400px; top: 856px; width: 760px; height: 170px; border-radius: 60px; background: linear-gradient(90deg, rgba(255,138,42,.95), rgba(247,242,122,.6)); display: flex; flex-direction: column; justify-content: center; padding: 0 40px; font-size: 29px; font-weight: 600; line-height: 1.35; text-align: right; }

  .shore { left: 0; top: 1040px; width: 1176px; height: 160px; background: linear-gradient(180deg, var(--c-sea) 0 70px, var(--c-sand) 70px); }
  .legend { top: 1080px; font-family: "Montserrat", sans-serif; font-weight: 700; font-size: 30px; color: var(--c-ink); }
  .legend--secure { left: 232px; }
  .legend--cancer { left: 590px; }
  .legend--melanoma { left: 990px; }
  .legend-mark { width: 44px; height: 44px; border-radius: 8px; border: 6px solid var(--c-frame); top: 1128px; }
  .legend-mark--secure { left: 258px; background: var(--c-towel); }
  .legend-mark--cancer { left: 650px; background: var(--c-cancer); }
  .legend-mark--melanoma { left: 1040px; background: var(--c-melanoma); }

  .beach-grid { left: 28px; top: 1200px; width: 1120px; height: 1110px; display: grid; grid-template-columns: repeat(10, 1fr); grid-template-rows: repeat(10, 1fr); gap: 8px; }
  .spot { position: relative; border: 7px solid var(--c-frame); border-radius: 8px; background: var(--c-towel); box-shadow: inset 0 0 0 8px #f7c98a; }
  .spot.is-cancer { background: var(--c-cancer); box-shadow: inset 0 0 0 8px #f36a55; }
  .spot.is-melanoma { background: var(--c-melanoma); box-shadow: inset 0 0 0 8px #a31a30; }
  .spot.is-melanoma::after { content: ""; position: absolute; left: 50%; top: 50%; transform: translate(-50%,-55%); border-left: 18px solid transparent; border-right: 18px solid transparent; border-bottom: 30px solid var(--c-white); }

  .prevent-title { left: 0; width: 1176px; top: 2366px; text-align: center; font-size: 50px; }
  .prevent-rule { left: 70px; top: 2440px; width: 1036px; height: 8px; background: var(--c-white); border-radius: 4px; }
  .intro { left: 90px; width: 996px; top: 2500px; text-align: center; font-size: 28px; line-height: 1.5; }

  .tip-title { font-family: "Montserrat", sans-serif; font-weight: 700; font-size: 34px; }
  .tip-text { font-size: 28px; line-height: 1.45; }

  .clock { left: 60px; top: 2650px; width: 220px; height: 220px; }
  .tip-title--sun { left: 316px; top: 2696px; }
  .tip-text--sun { left: 368px; top: 2760px; width: 420px; }

  .art--doctor { left: 820px; top: 2940px; width: 330px; height: 470px; background: linear-gradient(180deg, #f0f0f6, #c9c4dd); }
  .art--sunscreen { left: 60px; top: 2980px; width: 220px; height: 340px; background: linear-gradient(180deg, #ffb43a, #f08a1a); border-radius: 20px; }
  .tip-title--screen { left: 390px; top: 2996px; }
  .tip-text--screen { left: 370px; top: 3100px; width: 420px; }

  .art--hat { left: 30px; top: 3400px; width: 280px; height: 380px; background: linear-gradient(180deg, #f7a3c5, #e0559a); }
  .tip-title--cloth { left: 430px; top: 3440px; }
  .tip-text--cloth { left: 370px; top: 3510px; width: 680px; }

  .art--island { left: 930px; top: 3700px; width: 230px; height: 240px; background: linear-gradient(180deg, #3d3a9e, #f3e6c8); }
  .art--bed-bolt { left: 60px; top: 3840px; width: 140px; height: 320px; background: linear-gradient(180deg, #ff4f8e, #e2c1ff); border-radius: 20px; }
  .tip-title--beds { left: 470px; top: 3840px; }
  .tip-text--beds { left: 430px; top: 3910px; width: 470px; }

  .art--magnifier { left: 910px; top: 4030px; width: 250px; height: 170px; background: linear-gradient(135deg, #f5c6a4, #3aa0e8); }
  .tip-title--check { left: 0; width: 1176px; top: 4210px; text-align: center; }
  .tip-text--check { left: 0; width: 1176px; top: 4300px; text-align: center; }
</style>
</head>
<body>
<main class="poster">
  <h1 class="abs title heading">Skin Cancer</h1>
  <div class="abs title-rule"></div>

  <div class="abs art art--bolt" role="img" aria-label="Lightning bolt illustration representing ultraviolet light"></div>
  <p class="abs bubble bubble--cause">The primary cause of skin cancer is exposure to ultraviolet (UV) light from the sun or indoor tanning.</p>
  <div class="abs bubble-pill"></div>
  <p class="abs bubble bubble--exposure">The greater the total amount of sun exposure over a lifetime, the greater the chance of melanoma.</p>
  <div class="abs dot dot--a"></div>
  <div class="abs dot dot--b"></div>
  <div class="abs art art--walker" role="img" aria-label="Illustration of a woman in a red dress walking on a beach with palm trees"></div>

  <div class="abs art art--lounger" role="img" aria-label="Illustration of a man in sunglasses relaxing on the beach"></div>
  <p class="abs ask ask--likely">How likely are you to get skin cancer?</p>
  <p class="abs ask ask--beach">Let's say 100 people go to the beach...</p>
  <p class="abs ask ask--count"><span>How many will develop skin cancer in their lifetime?</span><span>How many will develop melanoma, the deadliest form of skin cancer?</span></p>

  <div class="abs shore" role="img" aria-label="Beach scene with sea, sand, umbrellas and towels"></div>
  <span class="abs legend legend--secure">Secure</span>
  <span class="abs legend legend--cancer">Skin cancer</span>
  <span class="abs legend legend--melanoma">Melanoma</span>
  <div class="abs legend-mark legend-mark--secure"></div>
  <div class="abs legend-mark legend-mark--cancer"></div>
  <div class="abs legend-mark legend-mark--melanoma"></div>

  <section class="abs beach-grid" aria-label="100 beach towels: 20 develop skin cancer, 3 of them melanoma">
    <div class="spot"></div><div class="spot"></div><div class="spot is-cancer"></div><div class="spot"></div><div class="spot"></div><div class="spot"></div><div class="spot"></div><div class="spot"></div><div class="spot is-cancer"></div><div class="spot"></div>
    <div class="spot"></div><div class="spot"></div><div class="spot"></div><div class="spot"></div><div class="spot"></div><div class="spot is-cancer"></div><div class="spot"></div><div class="spot"></div><div class="spot"></div><div class="spot is-cancer is-melanoma"></div>
    <div class="spot is-cancer"></div><div class="spot"></div><div class="spot"></div><div class="spot"></div><div class="spot"></div><div class="spot"></div><div class="spot is-cancer"></div><div class="spot"></div><div class="spot"></div><div class="spot"></div>
    <div class="spot"></div><div class="spot"></div><div class="spot"></div><div class="spot is-cancer"></div><div class="spot"></div><div class="spot"></div><div class="spot"></div><div class="spot is-cancer"></div><div class="spot"></div><div class="spot"></div>
    <div class="spot"></div><div class="spot is-cancer is-melanoma"></div><div class="spot"></div><div class="spot"></div><div class="spot"></div><div class="spot"></div><div class="spot"></div><div class="spot"></div><div class="spot"></div><div class="spot is-cancer"></div>
    <div class="spot"></div><div class="spot"></div><div class="spot"></div><div class="spot"></div><div class="spot is-cancer"></div><div class="spot"></div><div class="spot"></div><div class="spot"></div><div class="spot is-cancer"></div><div class="spot"></div>
    <div class="spot is-cancer"></div><div class="spot"></div><div class="spot"></div><div class="spot"></div><div class="spot"></div><div class="spot"></div><div class="spot is-cancer is-melanoma"></div><div class="spot"></div><div class="spot"></div><div class="spot"></div>
    <div class="spot"></div><div class="spot"></div><div class="spot is-cancer"></div><div class="spot"></div><div class="spot"></div><div class="spot"></div><div class="spot"></div><div class="spot is-cancer"></div><div class="spot"></div><div class="spot"></div>
    <div class="spot"></div><div class="spot"></div><div class="spot"></div><div class="spot"></div><div class="spot is-cancer"></div><div class="spot"></div><div class="spot"></div><div class="spot"></div><div class="spot"></div><div class="spot is-cancer"></div>
    <div class="spot"></div><div class="spot is-cancer"></div><div class="spot"></div><div class="spot"></div><div class="spot"></div><div class="spot"></div><div class="spot is-cancer"></div><div class="spot"></div><div class="spot"></div><div class="spot"></div>
  </section>

  <h2 class="abs prevent-title heading">What can you do to prevent skin cancer ?</h2>
  <div class="abs prevent-rule"></div>
  <p class="abs intro">Leading medical experts, including those at Halvern Clinic, make these recommendations for preventing skin cancer:</p>

  <svg class="abs clock" viewBox="0 0 220 220" role="img" aria-label="Clock chart highlighting 10 a.m. to 4 p.m.">
    <circle cx="110" cy="110" r="96" fill="none" stroke="#ff2a2a" stroke-width="6"/>
    <path d="M110 110 L110 24 A86 86 0 0 1 184 67 Z" fill="#ff3b3b"/>
    <path d="M110 110 L184 67 A86 86 0 0 1 196 110 Z" fill="#ffd23a"/>
    <path d="M110 110 L196 110 A86 86 0 0 1 184 153 Z" fill="#ff8a2a"/>
    <path d="M110 110 L184 153 A86 86 0 0 1 110 196 Z" fill="#2fb35a"/>
    <path d="M110 110 L110 196 A86 86 0 0 1 36 153 Z" fill="#3a7be8"/>
    <path d="M110 110 L36 153 A86 86 0 0 1 36 67 Z" fill="#ffe88a"/>
    <path d="M110 110 L36 67 A86 86 0 0 1 110 24 Z" fill="#ff6a3a"/>
    <text x="6" y="34" font-family="Montserrat, sans-serif" font-size="26" font-weight="700" fill="#ffffff">10</text>
    <text x="196" y="206" font-family="Montserrat, sans-serif" font-size="26" font-weight="700" fill="#ffffff">4</text>
  </svg>
  <h3 class="abs tip-title tip-title--sun">Avoid the sun from 10 a.m. to 4 p.m.</h3>
  <p class="abs tip-text tip-text--sun">These are the peak hours of sun strength in North America–even in the winter and on cloudy days.</p>

  <div class="abs art art--doctor" role="img" aria-label="Illustration of a doctor in a white coat"></div>

  <div class="abs art art--sunscreen" role="img" aria-label="Illustration of a sunscreen tube with a shield"></div>
  <h3 class="abs tip-title tip-title--screen">Wear sunscreen</h3>
  <p class="abs tip-text tip-text--screen">Reapply sunscreen every two hours or more frequently if you're swimming or sweating.</p>

  <div class="abs art art--hat" role="img" aria-label="Illustration of a head wearing a wide brimmed hat"></div>
  <h3 class="abs tip-title tip-title--cloth">Wear protective clothing</h3>
  <p class="abs tip-text tip-text--cloth">Hats with wide brims and clothing that covers your arms and legs are helpful. Sunscreen doesn't block all UV rays, Which cause skin cancer.</p>

  <div class="abs art art--island" role="img" aria-label="Illustration of a small island with palm trees"></div>
  <div class="abs art art--bed-bolt" role="img" aria-label="Illustration of a lightning bolt over a tanning lamp"></div>
  <h3 class="abs tip-title tip-title--beds">Avoid tanning beds</h3>
  <p class="abs tip-text tip-text--beds">Tannings beds operate with UV lights, damaging your skin and potentially leading to cancer.</p>

  <div class="abs art art--magnifier" role="img" aria-label="Illustration of a hand holding a magnifying glass"></div>
  <h3 class="abs tip-title tip-title--check">Self-check your skin</h3>
  <p class="abs tip-text tip-text--check">If you notice differences, talk with your health care team.</p>
</main>
</body>
</html>
```